LumaroVision.com

3D Advertising Agency. We Bring Brands to Life! We provide the most advanced No Glasses Needed 3D digital displays for advertising. Our multi-media experts produce the most stunning and impressive advertising for brands in 3D and consumers get the experience of a lifetime when they see our displays Without Glasses! The website need to look eye-catching, creative and vibrant! Our glasses free 3D displays leave a long lasting impression and create the ultimate consumer experience! We need to look BIG, we need to look INNOVATIVE, CUTTING EDGE and ready to deliver. Please see website examples in comments section. http://thekvpstudio.co.uk/ has nice wire frame.
http://www.brightwallscreens.com/media/sports.html has good secondary content page layouts and calls to action.
Updates

Take a look at this design and content.  This is my competition. http://www.nexodepthview.com/About+Us

http://www.qolvenscreens.com/

competitor

This company http://www.parvolenzusa.com/ is my partner and I am a reseller for them.  I don't want to look like them 100%, they manufacture, we are a solutions provider.

MAKE ME LOOK LIKE THIS! http://thekvpstudio.co.uk/

TOP NAVIGATION SHOULD ONLY INCLUDE THESE:

SOLUTION, MEDIA, SERVICES, ABOUT US

Target Market(s)

Casinos, NightClubs, bars, movie theaters,Fortune 500 consumer brands, Entertainment, Sports and Fashion Leaders.

Industry/Entity Type

Advertising

Requirements
Must have
• 3D effects, Flash, Dynamic imagery, clean and not too busy!
Nice to have
• Must make our logo's color symbol come to life with flash.

```html
<!DOCTYPE html>
<html lang="en">
<head>
<meta charset="utf-8">
<title>LumaroVision — 3D Advertising Solutions</title>
<link href="https://fonts.googleapis.com/css2?family=Noto+Sans:wght@400;700&family=Arimo:wght@400&display=swap" rel="stylesheet">
<style>
:root{
  --header:#3e6892;
  --header-deep:#2f5479;
  --hero-top:#4f7fab;
  --hero-bottom:#7fa6c9;
  --slide-a:#6d8799;
  --slide-b:#98a39a;
  --page:#ffffff;
  --ink:#2b2b2b;
  --muted:#555;
  --link:#2a95d6;
  --nav-active:#ffffff;
  --nav:#8fd0f5;
  --orange:#f05a12;
  --btn-top:#52b8f0;
  --btn-bottom:#1c86cf;
  --footer-top:#3a5f86;
  --footer-bottom:#284a6e;
  --footer-text:#c9d8e8;
  --footer-bar:#21405f;
  --tick:#2db44a;
}
*{margin:0;padding:0;box-sizing:border-box}
html,body{width:952px;height:1200px;overflow:hidden;background:var(--page)}
body{position:relative;font-family:"Arimo",Arial,sans-serif;color:var(--ink)}
h2,h3{font-weight:400}
.abs{position:absolute}

/* header */
.site-header{left:0;top:0;width:952px;height:66px;background:linear-gradient(var(--header),var(--header-deep));border-bottom:1px solid #27486b}
.brand{left:61px;top:14px;display:flex;align-items:center;gap:8px}
.brand-dot{width:30px;height:30px;border-radius:50%;background:#2e8fd8}
.brand-name{font-family:"Noto Sans",sans-serif;font-size:15px;color:#fff}
.main-nav{right:86px;top:21px;display:flex;gap:19px;font-family:"Noto Sans",sans-serif;font-size:12.5px}
.main-nav a{color:var(--nav);text-decoration:none}
.main-nav a.current{color:var(--nav-active)}

/* hero */
.hero-band{left:0;top:66px;width:952px;height:290px;background:linear-gradient(var(--hero-top),var(--hero-bottom))}
.hero-below{left:0;top:356px;width:952px;height:110px;background:linear-gradient(#e9eef2,#fff)}
.slider{left:63px;top:115px;width:831px;height:294px;background:#1f3347;padding:4px}
.slide-art{width:100%;height:100%;background:linear-gradient(135deg,var(--slide-a),var(--slide-b))}
.slider-dots{left:77px;top:385px;display:flex;gap:6px}
.slider-dots span{width:9px;height:9px;border-radius:50%;background:#e8e8e8}
.slider-shadow{left:80px;top:425px;width:800px;height:32px;border-radius:50%;background:radial-gradient(ellipse at center,rgba(0,0,0,.28),rgba(0,0,0,0) 70%)}

/* call to action */
.cta-bar{left:63px;top:466px;width:831px;height:48px;border:1px solid #dde2e6;border-radius:4px;background:linear-gradient(#fbfbfb,#eceef0)}
.cta-text{left:82px;top:477px;font-family:"Noto Sans",sans-serif;font-weight:700;font-size:18.5px;color:var(--orange)}
.cta-button{left:716px;top:475px;width:158px;height:33px;border-radius:3px;background:linear-gradient(var(--btn-top),var(--btn-bottom));color:#fff;font-family:"Noto Sans",sans-serif;font-size:19px;text-align:center;line-height:33px;letter-spacing:.5px}

/* intro columns */
.col-title{font-family:"Noto Sans",sans-serif;font-size:15.5px;line-height:19px;color:#222}
.col-text{font-size:11px;line-height:16.5px;color:var(--muted);letter-spacing:.2px}
.col-text a{color:var(--link);text-decoration:none}
.col-text b{color:#333}
.icon{width:34px;height:34px}
.serve-list{list-style:none}
.serve-list li{position:relative;padding-left:33px;margin-bottom:16px}
.serve-list svg{position:absolute;left:0;top:0}
.divider{left:62px;top:740px;width:830px;height:1px;background:linear-gradient(90deg,transparent,#d5d5d5 20%,#d5d5d5 80%,transparent)}

/* portfolio */
.thumb{width:182px;height:113px}
.thumb-more{width:28px;height:28px;border-radius:50%;background:linear-gradient(#fff,#d8d8d8);border:1px solid #bbb;box-shadow:0 1px 3px rgba(0,0,0,.3)}
.item-title{font-size:11px;color:var(--link)}
.item-desc{font-size:11px;color:#333}

/* footer */
.site-footer{left:0;top:964px;width:952px;height:203px;background:linear-gradient(var(--footer-top),var(--footer-bottom))}
.foot-title{font-family:"Noto Sans",sans-serif;font-size:15.5px;color:#fff;white-space:nowrap}
.foot-text{font-size:10.5px;line-height:13px;color:var(--footer-text);letter-spacing:.2px}
.foot-text a{color:#5cc0f2;text-decoration:none}
.foot-text .white{color:#fff}
.social{display:flex;gap:9px}
.social span{width:27px;height:27px;border-radius:50%}
.contact-button{left:711px;top:1086px;width:178px;height:48px;border-radius:3px;background:linear-gradient(#2e4e70,#1c3856);border:1px solid #456a90;color:#5cc0f2;font-family:"Noto Sans",sans-serif;font-size:24px;text-align:center;line-height:46px}
.footer-bar{left:0;top:1167px;width:952px;height:33px;background:var(--footer-bar);border-top:1px solid #3b5f84}
.footer-nav{left:66px;top:1178px;display:flex;gap:29px;font-family:"Noto Sans",sans-serif;font-size:10px}
.footer-nav a{color:#5cb4e6;text-decoration:none}
.copyright{right:56px;top:1178px;font-family:"Noto Sans",sans-serif;font-size:9.5px;color:#e6edf4;letter-spacing:.3px}
</style>
</head>
<body>

<header class="site-header abs">
  <div class="brand abs"><span class="brand-dot"></span><span class="brand-name">LumaroVision</span></div>
  <nav class="main-nav abs">
    <a class="current" href="#">Solutions</a><a href="#">Media</a><a href="#">Services</a><a href="#">About Us</a>
  </nav>
</header>

<div class="hero-band abs"></div>
<div class="hero-below abs"></div>
<div class="slider-shadow abs"></div>
<div class="slider abs">
  <div class="slide-art" role="img" aria-label="3D advertising scene: giant wheel with colourful flags and floating balloons at sunset"></div>
</div>
<div class="slider-dots abs"><span></span><span></span><span></span></div>

<div class="cta-bar abs"></div>
<div class="cta-text abs">3D Advertising Solutions to Drive Revenue and Brand Performance!</div>
<div class="cta-button abs">Get Started</div>

<section class="abs" style="left:62px;top:545px;width:210px">
  <h2 class="col-title">Welcome to lumarovision<br>Your multimedia expert</h2>
  <p class="col-text" style="margin-top:14px;padding-left:2px">We add value for our clients by provid-ing 3D advertising systems that drive top line revenue and Enhance their Consumer Brand Experience.<br><br><a href="#">View More</a></p>
</section>

<section class="abs" style="left:295px;top:545px;width:195px">
  <svg class="icon abs" style="left:0;top:0" viewBox="0 0 34 34"><rect x="2" y="3" width="30" height="21" rx="3" fill="#3b4a58"/><rect x="5" y="6" width="24" height="15" fill="#5fc6ee"/><rect x="13" y="25" width="8" height="4" fill="#555"/><rect x="8" y="29" width="18" height="3" rx="1" fill="#444"/></svg>
  <h2 class="col-title" style="margin-left:54px">Lumarovision<br>Featured Service</h2>
  <p class="col-text" style="margin-top:14px">Unlike other traditional digital advertis-ing method, at lumarovision you can :<br><br><a href="#">Produces a vivid and unforgettable</a><br><br><a href="#">Drive Brand Innovation &amp; Thought Leadership</a></p>
</section>

<section class="abs" style="left:504px;top:545px;width:196px">
  <svg class="icon abs" style="left:0;top:0" viewBox="0 0 34 34"><polygon points="17,1 21,11 32,11 23,18 27,30 17,23 7,30 11,18 2,11 13,11" fill="#3fb3d9"/><circle cx="17" cy="17" r="6" fill="#a9e7f7"/></svg>
  <h2 class="col-title" style="margin-left:54px">Why you should<br>Choose us</h2>
  <p class="col-text" style="margin-top:14px"><b>The “Branding Model-”</b> is used by a business to promote their own products, services or events.<br><br><b>The “Advertising Model”</b>-features ads that are paid for display by suppli-ers of products or services.</p>
</section>

<section class="abs" style="left:712px;top:545px;width:205px">
  <svg class="icon abs" style="left:1px;top:1px" viewBox="0 0 34 34"><circle cx="17" cy="17" r="15" fill="#3f7fc6"/><ellipse cx="17" cy="12" rx="13" ry="6" fill="#82b8ea" opacity=".6"/></svg>
  <h2 class="col-title" style="margin-left:57px">Who we serve<br>A Best in 3D adv.</h2>
  <ul class="serve-list col-text" style="margin-top:14px">
    <li><svg width="16" height="16" viewBox="0 0 16 16" style="top:6px"><circle cx="8" cy="8" r="8" fill="var(--tick)"/><path d="M4 8.3l2.7 2.6L12 5.5" stroke="#fff" stroke-width="2" fill="none"/></svg>Restaurants, Bars, Night Clubs, Casinos Entertainment venues</li>
    <li><svg width="16" height="16" viewBox="0 0 16 16" style="top:6px"><circle cx="8" cy="8" r="8" fill="var(--tick)"/><path d="M4 8.3l2.7 2.6L12 5.5" stroke="#fff" stroke-width="2" fill="none"/></svg>Brands in the Sports, Music, Entertainment,Consumer goods</li>
    <li style="margin-top:-6px"><svg width="16" height="16" viewBox="0 0 16 16"><circle cx="8" cy="8" r="8" fill="var(--tick)"/><path d="M4 8.3l2.7 2.6L12 5.5" stroke="#fff" stroke-width="2" fill="none"/></svg>Location HIGH traffic Activity</li>
  </ul>
</section>

<div class="divider abs"></div>

<section class="abs" style="left:62px;top:770px;width:200px">
  <h2 class="col-title">Recent Portfolios</h2>
  <p class="col-text" style="margin-top:9px;padding-left:2px">We build interactive customer acquisi-tion strategies using Performance Enhancing Ads.<br>Our experts have years of experience producing cutting edge 3D content</p>
</section>

<div class="thumb abs" style="left:293px;top:771px;background:linear-gradient(135deg,#2a343b,#6f7377)" role="img" aria-label="Modern living room with black and white sofas"></div>
<div class="thumb-more abs" style="left:455px;top:866px"></div>
<div class="item-title abs" style="left:293px;top:906px">Portfolio item title here</div>
<div class="item-desc abs" style="left:293px;top:920px">Short description placed here lorem</div>

<div class="thumb abs" style="left:503px;top:771px;background:linear-gradient(135deg,#5a4a3c,#b8a68e)" role="img" aria-label="Living room with a lattice screen wall and a beige sofa"></div>
<div class="thumb-more abs" style="left:670px;top:866px"></div>
<div class="item-title abs" style="left:504px;top:906px">Portfolio item title here</div>
<div class="item-desc abs" style="left:504px;top:920px">Short description placed here lorem</div>

<div class="thumb abs" style="left:713px;top:771px;background:linear-gradient(135deg,#c79a62,#7a4520)" role="img" aria-label="Warm lit living room with wooden floor and staircase"></div>
<div class="thumb-more abs" style="left:880px;top:866px"></div>
<div class="item-title abs" style="left:712px;top:906px">Recent cast studies title here</div>
<div class="item-desc abs" style="left:712px;top:920px">Short description placed here lorem</div>

<footer class="site-footer abs"></footer>

<section class="abs" style="left:61px;top:991px;width:200px">
  <h3 class="foot-title">LumaroVision Inc.</h3>
  <p class="foot-text" style="margin-top:22px;padding-left:2px">Brings Brands to Life using Glasses Free 3D! and generates a Higher ROI<br><br><span class="white">Call Today!</span><br>Dana Whitfield<br>555-014-2290</p>
</section>

<section class="abs" style="left:291px;top:991px;width:200px">
  <h3 class="foot-title">Latest news and update</h3>
  <p class="foot-text" style="margin-top:22px;padding-left:3px;width:170px">
    <a href="#">This is title news goes here</a><br>We have just lorem ipsum dolor sit amet elite lorem ipsum comod. la petote<br><br><a href="#">This news title goes here</a><br>Amet elite lorem ipsum comod. la petote</p>
</section>

<section class="abs" style="left:504px;top:991px;width:190px">
  <h3 class="foot-title">Latest on tweeter</h3>
  <svg class="abs" style="left:2px;top:48px" width="16" height="12" viewBox="0 0 16 12"><path d="M0 2l7 5 9-7-5 9-4 1z" fill="#9fb3c8"/></svg>
  <svg class="abs" style="left:2px;top:88px" width="16" height="12" viewBox="0 0 16 12"><path d="M0 2l7 5 9-7-5 9-4 1z" fill="#9fb3c8"/></svg>
  <p class="foot-text abs" style="left:28px;top:43px;width:160px">Lumarovision title tweet<br><a href="#">http://qk.ly/dfgPoi</a><br>Lumarovision title tweet and little longer than above<br><a href="#">http://qk.ly/b689BH</a></p>
</section>

<section class="abs" style="left:710px;top:991px;width:200px">
  <h3 class="foot-title">Connect with us</h3>
  <div class="social abs" style="left:2px;top:47px">
    <span style="background:#3fb3e8"></span><span style="background:#e9eef2"></span><span style="background:#f18a1c"></span><span style="background:#6a2a8e"></span>
  </div>
</section>
<div class="contact-button abs">Contact Us</div>

<div class="footer-bar abs"></div>
<nav class="footer-nav abs"><a href="#">Solutions</a><a href="#">Media</a><a href="#">Services</a><a href="#">About Us</a></nav>
<div class="copyright abs">Copyright 2011 by Lumarovision</div>

</body>
</html>
```